Webpage for co-working space for tech startups

We have an established co-working space in Aalborg Denmark where we have around 30 companies sharing office space. We are starting a new chapter for us and would like to have a new graphical image - new logo and new webpage, but keep the same name. The webpage should be professional, but also "fun", not too serious. We are all about working hard on our companies, but also taking some time off in between and being social and having fun. We are not corporate, but want to project the image that we are serious about what we do.

We currently have a black/red logo (see www.hivelane.dk or test.hivelane.dk), but are interesting in having a new logo design, so colour can be chosen freely. Currently our logo is a big HIVE and a little lane underneath the HIVE. The new logo will be one word "hivelane" with a small logo before or on top.

If we can make a good webpage for this project, then I have a second more simple project which is also a small single page wordpress site which I would also like to have made.

Target Market(s)

tech startups - relatively new companies, typically younger people 20-35 with a tech background - business or programming, preferably both

Industry/Entity Type

HIVE

Logo Text

hivelane

Coding

Coded - Design and coding required

Number of Pages Required

4 page

Font styles to use
Sans Serif

Colors

Designer to choose colors to be used in the design.

Requirements
Must have
• Wordpress CMS.
• Mobile and PC optimized
• 2 languages - English and Danish
• Four sections, could be four pages, or four sections of a single page.
• "Home", "Residents", "Our Working Space", "Our Event Space"
• Footer of page or pages should have contact information.
• "Home" has some information about who we are and what we do
• "Residents" has a list of all our residents - it should be possible to easily add and removed new / old residents - See one example here: http://test.hivelane.dk/en_GB/beboere/ or another example here: http://www.hivelane.dk/beboere/ - one of our colleagues http://copperyard.dk/startups/ or another one of our colleagues http://www.tidalmillhall.dk/residents/
• "Our working space" will have a description of our building, a map of where it is and a bunch of photos which show the different offices, meeting rooms and people working
• "Our events space" will have a description of our event spaces, details of cost + different arrangments of furniture, and lots of photos of events, see here for an example http://www.hivelane.dk/lej-vores-lokaler/
• Our current webpage - www.hivelane.dk was put together very quickly and has not really been optimized. We started a new webpage test.hivelane.dk, but it was never really finished.
• We are looking for a simple webpage, not too much going on. Examples of some of our colleagues in the business http://copperyard.dk/, http://www.tidalmillhall.dk/,
Nice to have
• http://www.tidalmillhall.dk/ is a really good template for us. If we can get something like this, we are happy.

```html
<!DOCTYPE html>
<html lang="en">
<head>
<meta charset="utf-8">
<title>Hivelane – Co-working space for startups</title>
<link rel="stylesheet" href="https://fonts.googleapis.com/css2?family=Raleway:wght@600;700;800&family=Open+Sans:ital,wght@0,400;0,600;0,700;1,600&display=swap">
<style>
  :root{
    --red:#c4161c;
    --ink:#1c1c1c;
    --text:#555555;
    --white:#ffffff;
    --line:#cfcfcf;
    --band:#262626;
    --footer:#1a1a1a;
    --muted:#bdbdbd;
  }
  *{margin:0;padding:0;box-sizing:border-box}
  html,body{width:1200px;height:2597px;overflow:hidden}
  body{position:relative;background:var(--white);font-family:"Open Sans",Arial,sans-serif;color:var(--text)}
  .abs{position:absolute}
  h1,h2,h3,.brand{font-family:"Raleway",Arial,sans-serif;color:var(--ink)}

  /* hero */
  .hero{left:0;top:0;width:1200px;height:648px;overflow:hidden}
  .hero-photo{position:absolute;inset:0;background:
      radial-gradient(ellipse 340px 420px at 520px 240px,#6b5e54 0%,rgba(60,52,46,0) 70%),
      linear-gradient(100deg,#2a2a2c 0%,#3d3a38 35%,#4a4440 55%,#2e2c2c 80%,#1e1f22 100%)}
  .hero-shade{position:absolute;inset:0;background:rgba(0,0,0,.28)}
  .brand{position:absolute;left:99px;top:44px;font-size:29px;font-weight:700;color:var(--white)}
  .nav{position:absolute;top:50px;left:0;width:1200px;height:24px;font-family:"Open Sans",Arial,sans-serif;font-size:16px;font-weight:600;color:var(--white)}
  .nav a{position:absolute;top:0;color:var(--white);text-decoration:none}
  .nav a.is-active{color:var(--red)}
  .nav .search{position:absolute;left:960px;top:2px}
  .nav .lang{position:absolute;left:1023px;top:0;display:flex;align-items:center;gap:8px}
  .hero-title{position:absolute;top:262px;width:1200px;text-align:center;font-family:"Raleway",Arial,sans-serif;font-weight:800;font-size:72px;color:var(--white);letter-spacing:1px}
  .hero-sub{position:absolute;top:364px;width:1200px;text-align:center;font-size:28px;color:var(--white)}
  .dots{position:absolute;top:571px;left:568px;display:flex;gap:4px}
  .dots span{width:14px;height:14px;border-radius:50%;border:2px solid var(--white)}
  .dots span.on{background:var(--white)}

  /* welcome */
  .section-title{width:1200px;left:0;text-align:center;font-size:38px;font-weight:800;letter-spacing:.5px}
  .rule{height:5px;background:var(--red)}
  .lead{left:190px;width:820px;top:848px;text-align:center;font-size:19.5px;font-weight:600;font-style:italic;line-height:33px;color:#3a3a3a}
  .intro{left:210px;width:780px;top:942px;text-align:center;font-size:15.5px;line-height:33px;color:var(--text)}

  /* feature cards */
  .card{top:1126px;width:317px}
  .card-photo{width:317px;height:225px}
  .card h3{margin-top:42px;font-size:26px;font-weight:800;letter-spacing:.3px}
  .card .rule{width:62px;margin-top:6px;height:4px}
  .card p{margin-top:22px;font-size:14.5px;line-height:27px;color:var(--text)}
  .btn{display:inline-block;margin-top:22px;height:43px;padding:0 18px;line-height:39px;border:2px solid var(--red);border-radius:22px;color:var(--red);font-size:14px;font-weight:700;text-transform:uppercase;text-decoration:none}

  .divider{left:99px;top:1703px;width:1002px;height:2px;background:var(--line)}

  /* sponsors */
  .sponsor{top:1901px;width:233px;height:99px;border:1px solid #c8c8c8;display:flex;align-items:center;justify-content:center;font-family:"Open Sans",Arial,sans-serif;font-weight:700;font-size:19px;color:#2b3a55;text-align:center}

  /* newsletter */
  .newsletter{left:0;top:2095px;width:1200px;height:251px;background:var(--band)}
  .newsletter h2{position:absolute;top:50px;width:1200px;text-align:center;color:var(--white);font-size:30px;font-weight:700;letter-spacing:.5px}
  .newsletter p{position:absolute;top:96px;width:1200px;text-align:center;color:#e6e6e6;font-size:15px}
  .field{position:absolute;left:291px;top:142px;width:471px;height:50px;background:var(--white);display:flex;align-items:center;gap:10px;padding-left:18px;font-size:14px;color:#444;text-transform:uppercase}
  .subscribe{position:absolute;left:762px;top:142px;width:147px;height:50px;background:var(--red);color:var(--white);font-weight:700;font-size:15px;text-align:center;line-height:50px;text-transform:uppercase}

  /* footer */
  .footer{left:0;top:2346px;width:1200px;height:251px;background:var(--footer);color:#e8e8e8}
  .contact{position:absolute;top:48px;display:flex;align-items:center;gap:16px;font-size:14px;line-height:23px}
  .icon-ring{width:45px;height:45px;border:2px solid #e8e8e8;border-radius:50%;display:flex;align-items:center;justify-content:center}
  .footer-links{position:absolute;top:126px;width:1200px;text-align:center;font-size:14.5px}
  .footer-links a{color:#e8e8e8;text-decoration:none}
  .footer-links .sep{margin:0 18px}
  .footer-rule{position:absolute;left:99px;top:176px;width:1002px;height:1px;background:#3a3a3a}
  .copyright{position:absolute;left:99px;top:202px;font-size:13px}
  .social{position:absolute;left:966px;top:197px;display:flex;gap:6px}
  .social span{width:30px;height:30px;border:1.5px solid #e8e8e8;border-radius:50%}
</style>
</head>
<body>

<header class="abs hero">
  <div class="hero-photo" role="img" aria-label="Photo of a smiling young man working on a laptop in a warm co-working café"></div>
  <div class="hero-shade"></div>
  <div class="brand">Hivelane</div>
  <nav class="nav">
    <a class="is-active" style="left:416px" href="#">Home</a>
    <a style="left:499px" href="#">Residents</a>
    <a style="left:610px" href="#">Our Working Space</a>
    <a style="left:797px" href="#">Our Event Space</a>
    <span class="search">
      <svg width="17" height="17" viewBox="0 0 17 17"><circle cx="7" cy="7" r="5.2" fill="none" stroke="#fff" stroke-width="2.4"/><line x1="11" y1="11" x2="15.5" y2="15.5" stroke="#fff" stroke-width="2.6" stroke-linecap="round"/></svg>
    </span>
    <span class="lang">
      <svg width="24" height="15" viewBox="0 0 24 15"><rect width="24" height="15" fill="#1f3f8f"/><rect x="10" width="4" height="15" fill="#fff"/><rect y="5.5" width="24" height="4" fill="#fff"/><rect x="11" width="2" height="15" fill="#c8102e"/><rect y="6.5" width="24" height="2" fill="#c8102e"/></svg>
      Eng
      <svg width="10" height="6" viewBox="0 0 10 6"><path d="M0 0h10L5 6z" fill="#fff"/></svg>
    </span>
  </nav>
  <h1 class="hero-title">HIVELANE</h1>
  <p class="hero-sub">We provide co-working space for startup companies</p>
  <div class="dots"><span class="on"></span><span></span><span></span><span></span></div>
</header>

<main>
  <h2 class="abs section-title" style="top:740px">WELCOME TO HIVELANE</h2>
  <div class="abs rule" style="left:514px;top:803px;width:172px"></div>

  <p class="abs lead">Hivelane will create inspiration, motivation, cohesion, attention, jobs and opportunities - and thereby contribute to Aalborg and North Jutland becoming a growth center.</p>
  <p class="abs intro">Hivelane Ravnsholm Hall office is run by the association Hivelane f.nm.ba which is a voluntary association. The association wishes to focus on scalable entrepreneurs in Nordjylland. With the start of the office community, the association has created a physical focal point for growth entrepreneurs. Here one can meet for dialogue, sparring and knowledge sharing.</p>

  <article class="abs card" style="left:99px">
    <div class="card-photo" role="img" aria-label="Photo of a bright white lounge with an armchair and a low round table" style="background:linear-gradient(135deg,#f1f1ef 0%,#dcdad6 55%,#b9b3aa 100%)"></div>
    <h3>RESIDENTS</h3>
    <div class="rule"></div>
    <p>At Hivelane Ravnsholm Hall we do not call the companies at the hall for renters - they are so much more than that.</p>
    <a class="btn" href="#">Read more</a>
  </article>

  <article class="abs card" style="left:441px">
    <div class="card-photo" role="img" aria-label="Photo of a team working together around a desk with laptops" style="background:linear-gradient(135deg,#7a6a62 0%,#b8a595 45%,#d9cbbd 70%,#8c7b70 100%)"></div>
    <h3>OUR WORKING SPACE</h3>
    <div class="rule"></div>
    <p>At Hivelane Ravnsholm Hall we do not call the companies at the hall for renters - they are so much more than that.</p>
    <a class="btn" href="#">Read more</a>
  </article>

  <article class="abs card" style="left:784px">
    <div class="card-photo" role="img" aria-label="Photo of guests mingling at an event in a glass-roofed hall" style="background:linear-gradient(160deg,#cfd6da 0%,#8e9aa0 40%,#4e5558 75%,#2f3335 100%)"></div>
    <h3>OUR EVENT SPACE</h3>
    <div class="rule"></div>
    <p>At Hivelane Ravnsholm Hall we do not call the companies at the hall for renters - they are so much more than that.</p>
    <a class="btn" href="#">Read more</a>
  </article>

  <div class="abs divider"></div>

  <h2 class="abs section-title" style="top:1780px">SPONSORS</h2>
  <div class="abs rule" style="left:554px;top:1840px;width:92px"></div>

  <div class="abs sponsor" style="left:99px">Northmark IP</div>
  <div class="abs sponsor" style="left:355px">Advokat Lindqvist</div>
  <div class="abs sponsor" style="left:611px">Fjordline Bank</div>
  <div class="abs sponsor" style="left:868px">Brenstrup Revision</div>
</main>

<section class="abs newsletter">
  <h2>SUBSCRIBE TO OUR NEWSLETTER</h2>
  <p>Register your email address to get &nbsp;information about us</p>
  <div class="field">
    <svg width="14" height="11" viewBox="0 0 14 11"><rect width="14" height="11" rx="1" fill="#555"/><path d="M0.5 1l6.5 5 6.5-5" fill="none" stroke="#fff" stroke-width="1.3"/></svg>
    Email address
  </div>
  <div class="subscribe">Subscribe</div>
</section>

<footer class="abs footer">
  <div class="contact" style="left:261px">
    <span class="icon-ring"><svg width="14" height="19" viewBox="0 0 14 19"><path d="M7 0a7 7 0 0 0-7 7c0 5 7 12 7 12s7-7 7-12a7 7 0 0 0-7-7z" fill="#e8e8e8"/><circle cx="7" cy="7" r="2.6" fill="#1a1a1a"/></svg></span>
    <span>Kestrelvej 4B<br>9000 Aalborg, Denmark</span>
  </div>
  <div class="contact" style="left:521px">
    <span class="icon-ring"><svg width="17" height="17" viewBox="0 0 24 24"><path d="M6.6 10.8a15.1 15.1 0 0 0 6.6 6.6l2.2-2.2a1 1 0 0 1 1-.25 11.4 11.4 0 0 0 3.6.57 1 1 0 0 1 1 1V20a1 1 0 0 1-1 1A17 17 0 0 1 3 4a1 1 0 0 1 1-1h3.5a1 1 0 0 1 1 1c0 1.25.2 2.45.57 3.57a1 1 0 0 1-.25 1z" fill="#e8e8e8"/></svg></span>
    <span>(+45) 20 11 47 36</span>
  </div>
  <div class="contact" style="left:738px">
    <span class="icon-ring"><svg width="19" height="14" viewBox="0 0 19 14"><rect width="19" height="14" rx="1.5" fill="#e8e8e8"/><path d="M1 1.5l8.5 6.5 8.5-6.5" fill="none" stroke="#1a1a1a" stroke-width="1.6"/></svg></span>
    <span>info@hivelane.dk</span>
  </div>

  <nav class="footer-links">
    <a href="#">Home</a><span class="sep">|</span><a href="#">Residents</a><span class="sep">|</span><a href="#">Our Working Space</a><span class="sep">|</span><a href="#">Our Event Space</a>
  </nav>
  <div class="footer-rule"></div>
  <p class="copyright">Copyrights © 2018, Hivelane All rights reserved.</p>
  <div class="social" aria-label="Social links"><span></span><span></span><span></span><span></span></div>
</footer>

</body>
</html>
```